Looking for updated Letterhead and Compliments Slips to go with our new updated logo. This stationary will be used for letters to suppliers and customers so needs to be practical while also quite classic.

We are an engineering company so needs to be clean and precise

Target Market(s)

SME'S and large automotive customers

Industry/Entity Type

Automotive

Font styles to use
Sans Serif

Colors
85acd3
0356a4
0792cd
33a6d7
85abd2
ffffff

Requirements
Must have
• Address details as below
• KT Fabrications Limited
• Hallmere Road
• Thornbury
• Eastmoorshire
• LP47 9XZ, UK
• Telephone: +44 (0)1632 960418
• Fax: +44 (0)1632 960733
• Email: sales@ktfabrications.example
• Web: www.ktfabrications.example
Nice to have
• Nice to have some element of being a British Manufacturer

```html
<!DOCTYPE html>
<html lang="en">
<head>
<meta charset="utf-8">
<title>KT Fabrications Stationery</title>
<link rel="stylesheet" href="https://fonts.googleapis.com/css2?family=Open+Sans:wght@400;500&display=swap">
<style>
  :root {
    --navy: #0356a4;
    --sky: #0792cd;
    --rule: #33a6d7;
    --ink: #2b2b2b;
    --paper: #ffffff;
    --backdrop: #e6e9ee;
  }
  * { margin: 0; padding: 0; box-sizing: border-box; }
  html, body {
    width: 1200px; height: 1200px; overflow: hidden;
    background: var(--backdrop);
    font-family: "Open Sans", Arial, sans-serif;
    color: var(--ink);
  }
  .canvas { position: relative; width: 1200px; height: 1200px; }
  .sheet {
    position: absolute;
    background: var(--paper);
    box-shadow: 0 2px 6px rgba(0,0,0,0.12);
  }
  .brand {
    display: flex; align-items: center; justify-content: center; gap: 8px;
    color: var(--navy);
    font-weight: 500;
    text-transform: uppercase;
    letter-spacing: 0.28em;
    white-space: nowrap;
  }
  .brand-dot {
    display: inline-block; border-radius: 50%;
    background: var(--sky);
  }
  .address { text-align: center; line-height: 1.45; }
  .address .company { color: var(--navy); }
  .contact-rule { border: 0; border-top: 1px solid var(--rule); }
  .contact { text-align: center; white-space: nowrap; }
  .contact .label { color: var(--sky); }

  /* Letterhead */
  .letterhead { left: 40px; top: 232px; width: 520px; height: 735px; }
  .letterhead .brand { position: absolute; top: 46px; left: 0; right: 0; font-size: 12px; }
  .letterhead .brand-dot { width: 9px; height: 9px; }
  .letterhead .footer { position: absolute; left: 12px; right: 12px; bottom: 14px; font-size: 9px; }
  .letterhead .address { margin-bottom: 4px; }
  .letterhead .address .company { color: var(--ink); }
  .letterhead .contact-rule { margin-bottom: 5px; }
  .letterhead .contact .label { color: var(--ink); }

  /* Compliments slip */
  .slip { left: 590px; top: 232px; width: 570px; height: 269px; }
  .slip .brand { position: absolute; top: 86px; left: 0; right: 0; font-size: 14px; }
  .slip .brand-dot { width: 10px; height: 10px; }
  .slip .greeting { position: absolute; top: 110px; left: 0; right: 0; text-align: center; font-size: 17px; }
  .slip .footer { position: absolute; left: 5px; right: 5px; bottom: 20px; font-size: 9.6px; }
  .slip .address { margin-bottom: 4px; }
  .slip .contact-rule { margin-bottom: 5px; }

  /* Envelope */
  .envelope { left: 590px; top: 682px; width: 570px; height: 247px; }
  .envelope .brand { position: absolute; top: 68px; left: 18px; font-size: 12px; justify-content: flex-start; }
  .envelope .brand-dot { width: 9px; height: 9px; }
  .envelope .return-address { position: absolute; left: 18px; top: 196px; font-size: 8.4px; line-height: 1.5; }
  .envelope .return-address .company { color: var(--navy); }
</style>
</head>
<body>
<main class="canvas">

  <section class="sheet letterhead" aria-label="Letterhead">
    <div class="brand"><span class="brand-dot"></span>KT Fabrications</div>
    <footer class="footer">
      <p class="address"><span class="company">KT Fabrications Limited</span><br>Hallmere Road, Thornbury, Eastmoorshire, LP47 9XZ, UK</p>
      <hr class="contact-rule">
      <p class="contact"><span class="label">T:</span> +44 (0)1632 960418 | <span class="label">F:</span> +44 (0)1632 960733 | <span class="label">E:</span> sales@ktfabrications.example | <span class="label">W:</span> www.ktfabrications.example</p>
    </footer>
  </section>

  <section class="sheet slip" aria-label="Compliments slip">
    <div class="brand"><span class="brand-dot"></span>KT Fabrications</div>
    <p class="greeting">With Compliments</p>
    <footer class="footer">
      <p class="address"><span class="company">KT Fabrications Limited</span><br>Hallmere Road, Thornbury, Eastmoorshire, LP47 9XZ, UK</p>
      <hr class="contact-rule">
      <p class="contact"><span class="label">T:</span> +44 (0)1632 960418 | <span class="label">F:</span> +44 (0)1632 960733 | <span class="label">E:</span> sales@ktfabrications.example | <span class="label">W:</span> www.ktfabrications.example</p>
    </footer>
  </section>

  <section class="sheet envelope" aria-label="Envelope">
    <div class="brand"><span class="brand-dot"></span>KT Fabrications</div>
    <p class="return-address"><span class="company">KT Fabrications Limited</span><br>Hallmere Road, Thornbury, Eastmoorshire, LP47 9XZ, UK</p>
  </section>

</main>
</body>
</html>
```